Lift display layouts for global brand

We need display layouts for different sizes and applications of display. All layouts must include an arrow and floor position number. I will upload some basic examples. We want these to look modern and really eye-catching but suitable for the space it is meant for.

By "layout" we mean design specifically created for the space - including arrow, floor number, widgets / background graphics etc.
Display type ONE 15" (1024 x 768 pixels)
a. Hotel theme layout (logo, floor position, arrow and simple weather widget) [Landscape]
b. Layout displaying live TV news broadcast or similar [Landscape]
Display type TWO 10.4” (800 x 600 pixels)
a. Shopping centre layout + shop advert in main space [Landscape]
b. Office tenant standard layout + business logo in main space [Portrait]
c. Spa / Leisure Centre Layout [Landscape]
Display type 38” (1920 x 540 pixels)
a. Airport/Train station layout + flight/train departure information in main space [Landscape]
b. Restaurant layout + Menu in main space [Portrait]
c. Shopping Centre layout + Centre map in main space [Landscape]
Display type 21.5” (1920 x 1080 pixels)
a. Skyscraper layout + lift buttons and building history text [Portrait]
Display type 7” (800x480)
a. Simple lift position indicator arrow and floor [Landscape]
b. Lift position indicator with arrow and showing pictogram (Alarm, Maintenance or similar) [Landscape]

```html
<!DOCTYPE html>
<html lang="en">
<head>
<meta charset="utf-8">
<title>Spa Lift Display – Floor 3</title>
<link rel="stylesheet" href="https://fonts.googleapis.com/css2?family=Playfair+Display:wght@900&family=Cinzel:wght@400;600&family=Roboto:wght@700&display=swap">
<style>
  :root {
    --navy-deep: #0d1628;
    --navy-light: #1f2d44;
    --gold: #c9a24a;
    --gold-light: #f3dc8e;
    --gold-dark: #a9802f;
    --panel-gold-top: #b98f3e;
    --panel-gold-bottom: #d8b86a;
    --white: #ffffff;
    --room-dark: #2a211c;
    --room-brown: #5a4536;
    --skin: #b98262;
    --towel: #ece7e1;
    --cream: #d9cbb8;
  }
  * { margin: 0; padding: 0; box-sizing: border-box; }
  html, body { width: 1200px; height: 900px; overflow: hidden; background: var(--white); }
  .display {
    position: relative;
    width: 1200px;
    height: 900px;
    overflow: hidden;
  }
  .brand-panel {
    position: absolute;
    left: 0; top: 0;
    width: 375px; height: 352px;
    background: radial-gradient(ellipse at 50% 35%, var(--navy-light), var(--navy-deep) 80%);
  }
  .brand-mark {
    position: absolute;
    left: 125px; top: 82px;
    width: 120px; height: 120px;
    border: 3px solid var(--gold);
  }
  .brand-name {
    position: absolute;
    left: 0; top: 276px;
    width: 100%;
    text-align: center;
    font-family: "Cinzel", serif;
    font-weight: 600;
    font-size: 34px;
    line-height: 1;
    letter-spacing: 2px;
    color: var(--gold);
  }
  .brand-tagline {
    position: absolute;
    left: 0; top: 316px;
    width: 100%;
    text-align: center;
    font-family: "Cinzel", serif;
    font-weight: 400;
    font-size: 12px;
    line-height: 1;
    letter-spacing: 5px;
    color: var(--gold);
  }
  .floor-panel {
    position: absolute;
    left: 0; top: 352px;
    width: 375px; height: 548px;
    background: linear-gradient(180deg, var(--panel-gold-top), var(--panel-gold-bottom));
  }
  .direction-arrow {
    position: absolute;
    left: 108px; top: 46px;
    width: 128px; height: 264px;
  }
  .floor-number {
    position: absolute;
    left: 0; top: 300px;
    width: 340px;
    text-align: center;
    font-family: "Roboto", Arial, sans-serif;
    font-weight: 700;
    font-size: 230px;
    line-height: 1;
    color: var(--white);
  }
  .spa-photo {
    position: absolute;
    left: 375px; top: 0;
    width: 825px; height: 900px;
    background:
      radial-gradient(ellipse 45% 30% at 88% 68%, var(--towel), transparent 70%),
      radial-gradient(ellipse 40% 18% at 35% 92%, var(--towel), transparent 75%),
      radial-gradient(ellipse 45% 28% at 45% 62%, var(--skin), transparent 75%),
      radial-gradient(ellipse 35% 40% at 92% 22%, var(--cream), transparent 75%),
      linear-gradient(135deg, var(--room-dark) 0%, var(--room-brown) 45%, #8c6a55 75%, var(--cream) 100%);
  }
  .offer {
    position: absolute;
    left: 428px; top: 40px;
    font-family: "Playfair Display", Georgia, serif;
    font-weight: 900;
    color: var(--gold-light);
    background: linear-gradient(180deg, var(--gold-light), var(--gold) 60%, var(--gold-dark));
    -webkit-background-clip: text;
    background-clip: text;
    -webkit-text-fill-color: transparent;
  }
  .offer-line {
    font-size: 50px;
    line-height: 1.2;
    white-space: nowrap;
  }
  .offer-price {
    font-size: 112px;
    line-height: 1.05;
  }
</style>
</head>
<body>
  <main class="display">
    <section class="brand-panel">
      <div class="brand-mark"></div>
      <div class="brand-name">HOTEL NAME</div>
      <div class="brand-tagline">YOUR TAGLINE HERE</div>
    </section>

    <section class="floor-panel">
      <svg class="direction-arrow" viewBox="0 0 80 172" aria-label="Going up">
        <g fill="#ffffff">
          <polygon points="40,0 80,36 80,72 40,46 0,72 0,36"/>
          <polygon points="0,84 40,58 80,84 80,98 40,72 0,98"/>
          <polygon points="0,110 40,84 80,110 80,124 40,98 0,124"/>
          <polygon points="0,136 40,110 80,136 80,150 40,124 0,150"/>
        </g>
      </svg>
      <div class="floor-number">3</div>
    </section>

    <div class="spa-photo" role="img" aria-label="Photo of a couple relaxing on massage tables in a spa, with rolled towels, white orchids and a flower vase"></div>

    <div class="offer">
      <div class="offer-line">Book now for a FREE Pedicure</div>
      <div class="offer-line">with every treatment over</div>
      <div class="offer-price">£50</div>
    </div>
  </main>
</body>
</html>
```